Stationery and business cards - New design

I need following designs
- writing paper for business letters A4, you can take the data from our old paper. There should just be a place for a third bank account.
- writing paper for business letters (only design + logo, without address, bank accounts and legal data)
- business cards with qr code, one side, only German language (you can take the data from the old layout)

Target Market(s)

Industrial customers

Industry/Entity Type

sheet metal technology, laser cutting of metal sheet

Requirements
Must have
• The address above the recipient should be placed like on my old paper. No relationship to the old design (only color) - please make a completely new design.
Nice to have
• colors like in my new logo
Should not have
• - the business letter should be suitable for borderless print - the green timber in my old paper is very bad for this - so please make a design without a timber (or a timber like it is on my old paper)

```html
<!DOCTYPE html>
<html lang="de">
<head>
<meta charset="utf-8">
<title>Falkenrode Blechtechnik – Briefbogen</title>
<link href="https://fonts.googleapis.com/css2?family=Arimo:wght@400;700&family=Montserrat:wght@500;600;700&display=swap" rel="stylesheet">
<style>
  :root {
    --brand-blue: #004a8f;
    --brand-teal: #00858f;
    --ink: #111111;
    --paper: #ffffff;
  }
  * { margin: 0; padding: 0; box-sizing: border-box; }
  html, body { width: 850px; height: 1200px; overflow: hidden; background: var(--paper); }
  .letterhead {
    position: relative;
    width: 850px;
    height: 1200px;
    background: var(--paper);
    font-family: "Arimo", Arial, sans-serif;
    color: var(--ink);
  }
  .brand {
    position: absolute;
    left: 528px;
    top: 62px;
    display: flex;
    align-items: center;
    gap: 10px;
  }
  .brand-dot {
    width: 46px;
    height: 46px;
    border-radius: 50%;
    background: var(--brand-teal);
  }
  .brand-name {
    font-family: "Montserrat", sans-serif;
    font-weight: 700;
    font-size: 18px;
    line-height: 1.15;
    color: var(--brand-blue);
    letter-spacing: 0.5px;
  }
  .sender-address {
    position: absolute;
    left: 579px;
    top: 153px;
    font-family: "Montserrat", sans-serif;
    font-weight: 600;
    font-size: 14.2px;
    line-height: 15.7px;
    color: var(--brand-blue);
    font-style: normal;
  }
  .reference {
    position: absolute;
    left: 90px;
    top: 273px;
    font-size: 14.2px;
    line-height: 16.8px;
    display: grid;
    grid-template-columns: 69px auto;
  }
  .letter-body {
    position: absolute;
    left: 89px;
    top: 381px;
    width: 700px;
    font-size: 14.2px;
    line-height: 20.5px;
  }
  .letter-body p { margin-bottom: 41px; }
  .letter-body p.lead { text-indent: 37px; }
  .signatory {
    position: absolute;
    left: 567px;
    top: 898px;
    font-weight: 700;
    font-size: 15px;
  }
  .signature {
    position: absolute;
    left: 524px;
    top: 942px;
    width: 124px;
    height: 28px;
    background: linear-gradient(90deg, rgba(0,0,0,0.08), rgba(0,0,0,0.03));
    border-radius: 4px;
  }
  .footer {
    position: absolute;
    left: 0;
    top: 1092px;
    width: 850px;
    height: 108px;
  }
  .footer-shape { position: absolute; inset: 0; }
  .contact {
    position: absolute;
    display: flex;
    align-items: center;
    gap: 10px;
    font-family: "Montserrat", sans-serif;
    font-weight: 500;
    font-size: 17.5px;
    color: var(--paper);
    letter-spacing: 0.3px;
  }
  .contact svg { width: 18px; height: 18px; flex: none; }
  .contact-phone { left: 152px; top: 25px; }
  .contact-fax { left: 152px; top: 53px; }
  .contact-mail { left: 467px; top: 25px; }
  .contact-web { left: 467px; top: 53px; }
  .footer-mark {
    position: absolute;
    left: 752px;
    top: 12px;
    width: 57px;
    height: 57px;
    border-radius: 50%;
    border: 4px solid var(--paper);
  }
</style>
</head>
<body>
<main class="letterhead">
  <header class="brand">
    <div class="brand-dot"></div>
    <div class="brand-name">FALKENRODE<br>BLECHTECHNIK</div>
  </header>

  <address class="sender-address">
    Falkenrode Blechtechnik GmbH<br>
    Werkstraße 12<br>
    D-93170 Talheim
  </address>

  <div class="reference">
    <span>Lorem</span><span>: Ipsum dolor sit amet</span>
    <span>Consectu</span><span>: -</span>
    <span>Elit</span><span>: sed diam nonummy nibh euismod</span>
  </div>

  <section class="letter-body">
    <p class="lead">Lorem ipsum dolor sit amet consectetuer adipiscing elit, sed diam nonummy nibh euismod ncidunt<br>laoret dolore magna aliquam erat volutpat.Ut wisi enim ad minim veniam, quis nostrud exerci taion in<br>ullamcorper suscipit loboris nisl ut aliquip ex ea commodo cosesquat.Duis autem vel eum iriure dolor in<br>hendrerit in vulputate velit esse molesie consequat, vel illum dolore eu feugiat nulla facilisis at vero et<br>accumsan et iusto odio dignissim qui blandit praesent luptatum zzril delenit augue duis dolore fe feugait<br>nulla facilisi. Nam liber tempor cum soluta nobis eleifend opion congue nihil imperdiet doming id quod<br>mazim placerat facer possim asum.Typi non habent clartatem insita; est usus legenis in iis qui facit orum<br>claritatem.Invesigaiones demonstraverunt lectores legere me lius quod ii legunt saepius. Claritas est<br>eiam processus dynamicus, qui sequitur mutaionem consuetudium lectorum.Mirum est notare quam liter<br>a ghotica et quinta decima.Eodem modo typi,qui nunc nobis videntur parum clari, fiant spllemness in<br>futurum.</p>
    <p>Typi non habent claritatem insitam; est usus legenis in iss qui facit eorum claritatem. invesigaiones<br>demonstraverunt lecoter legere me lius quod ii legant sapius.Claritas est eiam prosessus dynamicus,<br>qui sequitur mutaionem consuetudium lectorum.Mirum est notare quam litera ghotica,quam nuns<br>putamus parum claram typi,qui nunc nobis videntur parum clari, fiant sollemnes in futurum.</p>
    <p>Typi non habent claritatem insitam; est usus legenis in iss qui facit eorum claritatem. invesigaiones<br>demonstraverunt lecoter legere me lius quod ii legant sapius.Claritas est eiam prosessus dynamicus,<br>qui sequitur mutaionem consuetudium lectorum.Mirum est notare quam litera ghotica,quam nuns<br>putamus parum claram typi,qui nunc nobis videntur parum clari, fiant sollemnes in futurum</p>
  </section>

  <div class="signatory">Director</div>
  <div class="signature" role="img" aria-label="Handwritten signature of the director"></div>

  <footer class="footer">
    <svg class="footer-shape" viewBox="0 0 850 108" preserveAspectRatio="none" aria-hidden="true">
      <path d="M0 0 H416 Q404 2 398 12 H0 Z" fill="var(--brand-teal)"/>
      <path d="M0 15 H402 Q412 0 442 0 H850 V108 H0 Z" fill="var(--brand-blue)"/>
    </svg>

    <div class="contact contact-phone">
      <svg viewBox="0 0 18 18"><rect width="18" height="18" rx="2" fill="#fff"/><path d="M6 4.5 C4.5 6 5 9 7.5 11.5 S12 14 13.5 12.5 L11.8 10.8 L10.5 11.6 C9.2 10.8 7.2 8.8 6.4 7.5 L7.2 6.2 Z" fill="var(--brand-blue)"/></svg>
      <span>+49(0)940012345-0</span>
    </div>
    <div class="contact contact-fax">
      <svg viewBox="0 0 18 18"><rect width="18" height="18" rx="2" fill="#fff"/><rect x="5" y="3.5" width="8" height="4" fill="var(--brand-blue)"/><rect x="4" y="8.5" width="10" height="6" rx="1" fill="var(--brand-blue)"/><rect x="6" y="10.5" width="6" height="1.2" fill="#fff"/></svg>
      <span>+49(0)940012345-429</span>
    </div>
    <div class="contact contact-mail">
      <svg viewBox="0 0 18 18"><rect width="18" height="18" rx="2" fill="#fff"/><rect x="3.5" y="5" width="11" height="8" rx="1" fill="var(--brand-blue)"/><path d="M3.8 5.5 L9 9.5 L14.2 5.5" stroke="#fff" stroke-width="1.1" fill="none"/></svg>
      <span>info@falkenrode-blt.de</span>
    </div>
    <div class="contact contact-web">
      <svg viewBox="0 0 18 18"><rect width="18" height="18" rx="2" fill="#fff"/><circle cx="9" cy="9" r="5.5" fill="var(--brand-blue)"/><path d="M3.5 9 H14.5 M9 3.5 V14.5" stroke="#fff" stroke-width="0.9"/></svg>
      <span>www.falkenrode-blt.de</span>
    </div>

    <div class="footer-mark"></div>
  </footer>
</main>
</body>
</html>
```